Redesign for Popular UK Town Website

We're looking for someone to redesign a website for a popular tourist town that's visited by over 250,000 people a year. We have a basic design frame in place and need someone to make it look more 'professional.'
We've created a temporary design layout to show you a general idea of what we're looking for: http://dorrin.co.uk/
All text/images are placeholder images so you can get an idea of the general layout.
(Please note that you can grab any images found on the internet for 'tenby' to be used as placeholder images. This is because we will be visiting the locations and taking our own photos, after the design is complete.)
Target Market(s)
Tourists
Industry/Entity Type
Town
Number of Pages Required
2 page
Requirements
Must have
- You need to redesign the homepage: http://dorrin.co.uk/
- You also need to redesign the following page: http://dorrin.co.uk/hotels/ (This page will be used for multiple categories and is used to list locations of properties/places etc.)
- Design must be responsive also.
Nice to have
- Please feel free to add as much as you can to the content/features as with our limited knowledge of websites, have only been able to create a basic layout.

```html
<!DOCTYPE html>
<html lang="en">
<head>
<meta charset="utf-8">
<title>Seaward – Visit Dorrin</title>
<link rel="stylesheet" href="https://fonts.googleapis.com/css2?family=Teko:wght@400&family=Raleway:wght@300;400;500;600&family=Open+Sans:ital,wght@0,400;0,600;0,700;1,400&display=swap">
<style>
:root{
  --sea:#0ea5ea;
  --sea-deep:#1b5fae;
  --ink:#222222;
  --muted:#555555;
  --paper:#ffffff;
  --mist:#f2f2f2;
  --footer:#333333;
  --footer-line:#5a5a5a;
  --footer-text:#e6e6e6;
}
*{box-sizing:border-box;margin:0;padding:0}
html,body{width:1200px;height:2486px;overflow:hidden}
body{position:relative;background:var(--paper);font-family:"Open Sans",Arial,sans-serif;color:var(--ink)}
.abs{position:absolute}

/* hero */
.hero{position:absolute;left:0;top:0;width:1200px;height:490px}
.hero-photo{position:absolute;left:0;top:0;width:643px;height:490px;
  background:linear-gradient(180deg,#5b9fd8 0%,#bcd9ef 26%,#3f6f93 34%,#7a8fa0 50%,#c9b27a 66%,#7d7060 82%,#4e4a42 100%)}
.brand{position:absolute;left:80px;top:50px;display:flex;align-items:center;gap:12px}
.brand-dot{width:54px;height:54px;border-radius:50%;background:#1d3f73}
.brand-name{font-family:"Raleway",sans-serif;font-weight:600;font-size:30px;color:#1d3f73}
.hero-panel{position:absolute;left:643px;top:0;width:557px;height:490px;background:var(--sea);color:#fff}
.search{position:absolute;left:28px;top:16px}
.locale{position:absolute;left:247px;top:19px;display:flex;align-items:center;gap:10px;font-size:13px;font-weight:600}
.flag{width:24px;height:14px;background:#f3c21b;position:relative}
.flag::before{content:"";position:absolute;left:7px;top:0;width:4px;height:14px;background:#174f9e}
.flag::after{content:"";position:absolute;left:0;top:5px;width:24px;height:4px;background:#174f9e}
.caret{font-size:10px;margin-left:4px}
.login{position:absolute;left:359px;top:15px;width:77px;height:28px;border:1px solid rgba(255,255,255,.85);border-radius:4px;font-size:12px;font-weight:600;display:flex;align-items:center;justify-content:center;gap:6px}
.burger{position:absolute;left:464px;top:20px;width:24px}
.burger span{display:block;height:3px;background:#fff;margin-bottom:5px}
.main-nav{position:absolute;left:17px;top:73px;display:flex;gap:29px;font-size:11px;font-weight:700;text-transform:uppercase;letter-spacing:.1px}
.hero-title{position:absolute;left:30px;top:135px;font-family:"Teko",sans-serif;font-size:90px;line-height:1;font-weight:400}
.hero-text{position:absolute;left:30px;top:249px;width:440px;font-size:14.6px;line-height:28px}

/* section heads */
.section-title{position:absolute;left:0;width:1200px;text-align:center;font-family:"Raleway",sans-serif;font-weight:300;font-size:43px;letter-spacing:1px;color:var(--ink)}
.section-sub{position:absolute;left:0;width:1200px;text-align:center;font-family:"Raleway",sans-serif;font-size:17px;color:var(--muted)}

/* tiles */
.tile{position:absolute;width:321px;overflow:hidden}
.tile-label{position:absolute;left:0;width:100%;text-align:center;color:#fff;font-family:"Raleway",sans-serif;font-size:18px;text-transform:uppercase}
.tile-icon{position:absolute;left:50%;width:43px;height:43px;margin-left:-21.5px;border-radius:50%;background:rgba(255,255,255,.9);display:flex;align-items:center;justify-content:center}
.tile-icon i{width:17px;height:17px;border-radius:50%;border:3px solid #2a74b8}
.tile-shade{position:absolute;left:0;bottom:0;width:100%;height:55%;background:linear-gradient(180deg,rgba(0,0,0,0),rgba(0,0,0,.7))}
.tile-highlight{position:absolute;left:23px;top:30px;width:273px;height:348px;background:var(--sea)}

/* offers */
.offers{position:absolute;left:0;top:1564px;width:1200px;height:653px;background:var(--mist)}
.offer{position:absolute;top:182px;width:313px;height:370px;background:#fff}
.offer-photo{height:196px;border-bottom:4px solid var(--sea-deep)}
.offer-title{position:absolute;left:17px;top:229px;font-family:"Open Sans",sans-serif;font-weight:700;font-size:16.5px;text-transform:uppercase}
.offer-text{position:absolute;left:17px;top:257px;width:285px;font-size:14px;line-height:23px}

/* footer */
.site-footer{position:absolute;left:0;top:2217px;width:1200px;height:269px;background:var(--footer);color:var(--footer-text)}
.footer-col{position:absolute;top:42px}
.footer-head{font-family:"Raleway",sans-serif;font-weight:600;font-size:21px;color:#fff}
.footer-rule{width:50px;height:3px;background:#5c8fd6;margin-top:10px}
.address{margin-top:22px;font-style:italic;font-size:11.5px;line-height:19px}
.copyright{margin-top:8px;font-size:11px;padding-top:8px;border-top:1px solid var(--footer-line);width:288px}
.contact-row{width:320px;height:31px;border-bottom:1px solid var(--footer-line);display:flex;justify-content:space-between;align-items:center;font-size:11px;text-transform:uppercase}
.contact-row:first-of-type{margin-top:20px;border-top:1px solid var(--footer-line)}
.contact-row em{font-weight:700}
.news-text{margin-top:26px;width:320px;font-size:10.5px;line-height:20px;text-transform:uppercase}
.news-form{margin-top:22px;display:flex}
.news-input{width:243px;height:28px;border:1px solid #8a8a8a;background:transparent}
.news-btn{width:58px;height:28px;background:var(--sea-deep);color:#fff;font-size:11px;display:flex;align-items:center;justify-content:center}
</style>
</head>
<body>

<header class="hero">
  <div class="hero-photo" role="img" aria-label="Photo of the harbour with moored boats, sandy beach and colourful houses on the cliff"></div>
  <div class="brand"><span class="brand-dot"></span><span class="brand-name">Seaward</span></div>
  <div class="hero-panel">
    <svg class="search" width="20" height="20" viewBox="0 0 20 20"><circle cx="8" cy="8" r="6" fill="none" stroke="#fff" stroke-width="2.5"/><line x1="12.5" y1="12.5" x2="18" y2="18" stroke="#fff" stroke-width="2.5" stroke-linecap="round"/></svg>
    <div class="locale"><span class="flag"></span><span>Dorrin<span class="caret">&#9660;</span></span></div>
    <div class="login"><svg width="10" height="12" viewBox="0 0 10 12"><rect x="0" y="5" width="10" height="7" rx="1" fill="#fff"/><path d="M2.5 5V3.5a2.5 2.5 0 0 1 5 0V5" fill="none" stroke="#fff" stroke-width="1.6"/></svg>Login</div>
    <div class="burger"><span></span><span></span><span></span></div>
    <nav class="main-nav"><span>Where to stay</span><span>Caravan &amp; Camping</span><span>Bed &amp; Breakfast</span><span>Hotels in Dorrin</span></nav>
    <h1 class="hero-title">Seaward</h1>
    <p class="hero-text">Welcome to Dorrin. The jewel in the crown of Carrowshire. A popular harbour town visited by over 299,000 visitors a year. Surrounded by its medieval stone wall, Dorrin is steeped with history and beautiful landscapes. Famed for it’s beautiful beaches and views that will lure you to come back each year, we hope you enjoy your time visiting and breathing in the sea air of Dorrin.</p>
  </div>
</header>

<h2 class="section-title" style="top:572px">WELCOME TO SEAWARD</h2>
<p class="section-sub" style="top:644px">Find inspiration for your holiday in Dorrin</p>

<div class="tile" style="left:80px;top:726px;height:255px;background:linear-gradient(180deg,#8fb3d6 0%,#c7b89a 40%,#6f6a5c 75%,#3b3a34 100%)" role="img" aria-label="Photo of the old harbour houses at the waterfront">
  <div class="tile-shade"></div><div class="tile-icon" style="top:160px"><i></i></div><div class="tile-label" style="top:218px">Things to do</div>
</div>
<div class="tile" style="left:80px;top:1017px;height:408px;background:linear-gradient(180deg,#d8e8f4 0%,#9cb8c8 50%,#5d8095 100%)" role="img" aria-label="Photo of the town seafront">
  <div class="tile-highlight"></div><div class="tile-icon" style="top:150px;background:transparent"><i style="border-color:#fff"></i></div><div class="tile-label" style="top:198px">Where to stay</div>
</div>
<div class="tile" style="left:437px;top:726px;height:409px;background:linear-gradient(180deg,#2b3440 0%,#8a6a5a 35%,#3a3030 70%,#111 100%)" role="img" aria-label="Photo of a restaurant table with a sculpture and city lights behind">
  <div class="tile-shade"></div><div class="tile-icon" style="top:300px"><i></i></div><div class="tile-label" style="top:362px">Places to eat</div>
</div>
<div class="tile" style="left:437px;top:1170px;height:255px;background:linear-gradient(180deg,#e8eef2 0%,#d9a86a 35%,#8b7a5a 65%,#2f2a22 100%)" role="img" aria-label="Photo of colourful houses above the harbour beach">
  <div class="tile-shade"></div><div class="tile-icon" style="top:148px"><i></i></div><div class="tile-label" style="top:202px">Skonne fiskeri-oplevelser</div>
</div>
<div class="tile" style="left:797px;top:726px;height:255px;background:linear-gradient(180deg,#3a78c8 0%,#a9c6e4 30%,#c9b08a 60%,#4a4036 100%)" role="img" aria-label="Photo of a narrow shopping street with flags">
  <div class="tile-shade"></div><div class="tile-icon" style="top:160px"><i></i></div><div class="tile-label" style="top:214px">Where to stay</div>
</div>
<div class="tile" style="left:797px;top:1017px;height:408px;background:linear-gradient(180deg,#b7c9c6 0%,#6f8a5a 30%,#c8b48e 55%,#1f4a44 80%,#0d1f1e 100%)" role="img" aria-label="Aerial photo of the headland town and beaches">
  <div class="tile-shade"></div><div class="tile-icon" style="top:310px"><i></i></div><div class="tile-label" style="top:372px">Vandreture i den danske natur</div>
</div>

<section class="offers">
  <h2 class="section-title" style="top:48px">CURRENT OFFERS FOR YOU</h2>
  <p class="section-sub" style="top:104px">Find inspiration for your holiday in Dorrin</p>
  <article class="offer" style="left:80px">
    <div class="offer-photo" style="background:linear-gradient(180deg,#a9c8e6 0%,#d89b5a 40%,#c9a878 70%,#6a6a58 100%)" role="img" aria-label="Photo of colourful houses and boats on the beach"></div>
    <h3 class="offer-title">Top 10 things to do in Dorrin</h3>
    <p class="offer-text">With tourist flocking to Dorrin every year, there’s never a shortage of things to do. This is our top 10 things to do in Dorrin and the surrounding area.</p>
  </article>
  <article class="offer" style="left:444px">
    <div class="offer-photo" style="background:linear-gradient(180deg,#c89aae 0%,#8c7f9a 35%,#6b5c66 65%,#3a3a46 100%)" role="img" aria-label="Photo of boats in the harbour at dusk"></div>
    <h3 class="offer-title">Top 10 things to do in Dorrin</h3>
    <p class="offer-text">With tourist flocking to Dorrin every year, there’s never a shortage of things to do. This is our top 10 things to do in Dorrin and the surrounding area.</p>
  </article>
  <article class="offer" style="left:804px">
    <div class="offer-photo" style="background:linear-gradient(90deg,#1f5a2a 0%,#a8382a 35%,#6a2a22 60%,#2a4a3a 100%)" role="img" aria-label="Photo of a couple beside a decorated Christmas tree"></div>
    <h3 class="offer-title">Top 10 things to do in Dorrin</h3>
    <p class="offer-text">With tourist flocking to Dorrin every year, there’s never a shortage of things to do. This is our top 10 things to do in Dorrin and the surrounding area.</p>
  </article>
</section>

<footer class="site-footer">
  <div class="footer-col" style="left:83px">
    <h4 class="footer-head">About Event</h4><div class="footer-rule"></div>
    <p class="address">Seaward<br>Havnevej 4, 2. tv. 1840 Eastholm<br>CVR nr: 40917326</p>
    <p class="copyright">Copyright 2016 &copy; Seaward &nbsp;All Rights Reserved</p>
  </div>
  <div class="footer-col" style="left:424px">
    <h4 class="footer-head">Contact Us</h4><div class="footer-rule"></div>
    <div class="contact-row"><span>Telephone</span><em>(012) 345-6789</em></div>
    <div class="contact-row"><span>Fax</span><em>(012) 345-6789</em></div>
    <div class="contact-row"><span>Reservation</span><em>(012) 345-6789</em></div>
  </div>
  <div class="footer-col" style="left:792px">
    <h4 class="footer-head">Newsletter</h4><div class="footer-rule"></div>
    <p class="news-text">Sign up for our newsletter, and we’ll keep you updated non all &nbsp;events flawless</p>
    <div class="news-form"><span class="news-input"></span><span class="news-btn">SEND</span></div>
  </div>
</footer>

</body>
</html>
```